Creative poster of core values for construction company

I'm looking for someone to design a 24in X 24in poster of our companies 5 core values. Using the 5 main words/phrases in a cool, exciting, graphic way.

The top of the art should read:
Harlow Construction Core Values

Those words/phrases are:
Passion and Ambition
Respect
Direct and honest
Shared Success
Family

Please incorporates Harlow Construction logo and brand colors. The final design will be signed by all of our associates and hung in our office. We want a poster that looks a little more like graphic art than just words on a page.

Maybe you add the key words within the Harlow H. Maybe you have the words repeat within the shape of the Harlow H. We want it creative.

Target Market(s)

Our employees.

Industry/Entity Type

Construction Company

Font styles to use
Sans Serif

Colors
ec1f27
000000
959595
fbfbfb

Requirements
Must have
• Must have Red (#e92a30) and bold aggressive feel.
• Should have some free spaces for associates to sign - does not need to explictly say sign here or anything.
Should not have
• This product should be easy to read.

```html
<!DOCTYPE html>
<html lang="en">
<head>
<meta charset="utf-8">
<title>Harlow Construction Core Values</title>
<link rel="stylesheet" href="https://fonts.googleapis.com/css2?family=Archivo:wght@900&display=swap">
<style>
  :root {
    --brand-red: #e1232a;
    --stripe-red: #e0292f;
    --ink: #000000;
    --paper: #fbfbfb;
  }
  html, body {
    margin: 0;
    padding: 0;
    width: 1200px;
    height: 1200px;
    overflow: hidden;
    background: var(--ink);
  }
  .poster {
    display: block;
    width: 1200px;
    height: 1200px;
  }
  .value,
  .brand-name {
    font-family: "Archivo", "Arial Black", sans-serif;
    font-weight: 900;
  }
  .value--black { fill: var(--ink); }
  .value--red { fill: var(--brand-red); }
  .brand-name { fill: var(--brand-red); }
</style>
</head>
<body>
<svg class="poster" viewBox="0 0 1200 1200" xmlns="http://www.w3.org/2000/svg" role="img" aria-label="Harlow Construction core values poster">
  <defs>
    <pattern id="hazard-stripes" patternUnits="userSpaceOnUse" width="69" height="69" patternTransform="rotate(61.5)">
      <rect width="69" height="69" fill="var(--paper)"/>
      <rect width="31" height="69" fill="var(--stripe-red)"/>
    </pattern>
  </defs>

  <rect class="frame-outer" x="0" y="0" width="1200" height="1200" fill="var(--ink)"/>
  <rect class="frame-stripes" x="81" y="81" width="1038" height="1038" fill="url(#hazard-stripes)"/>
  <rect class="signing-field" x="146" y="146" width="908" height="908" fill="var(--paper)"/>

  <g class="brand">
    <text class="brand-name" x="600" y="268" font-size="50" text-anchor="middle" textLength="520" lengthAdjust="spacingAndGlyphs">HARLOW CONSTRUCTION</text>
  </g>

  <g class="values">
    <text class="value value--black" x="255" y="407" font-size="77" textLength="739" lengthAdjust="spacingAndGlyphs">PASSION AND AMBITION</text>
    <text class="value value--red" x="495" y="502" font-size="131" textLength="474" lengthAdjust="spacingAndGlyphs">RESPECT</text>
    <text class="value value--black" x="180" y="571" font-size="99" textLength="838" lengthAdjust="spacingAndGlyphs">DIRECT AND HONEST</text>
    <text class="value value--red" x="213" y="652" font-size="113" textLength="796" lengthAdjust="spacingAndGlyphs">SHARED SUCCESS</text>
    <text class="value value--black" x="326" y="753" font-size="143" textLength="416" lengthAdjust="spacingAndGlyphs">FAMILY</text>
  </g>
</svg>
</body>
</html>
```